Web Page Design (Coded). Winner can expect additional work to implement

My current employer (www.halvertonholdings.com.au) requires the establishment of a new web page (www.halvertonbluegrid.com.au) to promote safety and environmental products which will be sold to the oil / gas / mining and environmental sectors. The web page needs to be somehow aligned with the parent company page above (if only the colouring to appease my boss), yet innovate and awesome. The successful designer will be expected to provide coded files and be able to provide additional services to edit and launch the website. The website is currently operational but the content and format are both poor. The website will be predominantly based around promoting our products but will include a "buy online" section for some products which will be part of the website, but on a different tab / layer. Video's and flash will be part of the successful web page. Actually, I know very little about web pages so just go for gold and make it good and make it work. I am not adding any files at this point in time, but do post a message if you require any files.

Target Market(s)

Our products will be promoted to customers in Australia and SE Asia in the mining, oil and gas sectors predominantly with local government also a purchaser. Most purchase decisions will be made by males and people needing to solve problems quickly. They often won't care what product they receive as long as it does the job.

Industry/Entity Type

Safety

Requirements
Must have
• Must be aligned with our parent company page design (www.halvertonholdings.com.au). When I say aligned, I am talking effectively about fonts and colouring. The page design itself can be innovative beyond the parent company page design.
Somewhere on the page it must say we are a division of Halverton Holdings Pty Ltd.
Nice to have
• Easy to find products, read about them and download brochures. Links to be provided to "buy online" or "request a quote" next to each product, but without pricing.
It is essential that contacting us by phone, email etc... is easy to find through every layer of the page. This is essential. We would like some photo's on the home page scrolling through products, but these do not need to be large. Our current website (halvertonbluegrid.com.au) has photo's but they are too big.

```html
<!DOCTYPE html>
<html lang="en">
<head>
<meta charset="utf-8">
<title>Halverton Blue Grid — Distributor of Disaster Management Technologies</title>
<link href="https://fonts.googleapis.com/css2?family=Raleway:wght@400;600;700;800&family=Open+Sans:wght@600;700&family=Open+Sans+Condensed:wght@700&family=Lora:ital,wght@1,600&display=swap" rel="stylesheet">
<style>
:root{
  --navy:#1b2a52;
  --gold:#e3ac48;
  --green:#9ccb8a;
  --ink:#333333;
  --muted:#9a9a9a;
  --soft:#f4f4f4;
  --white:#ffffff;
}
*{margin:0;padding:0;box-sizing:border-box}
html,body{width:1200px;height:2232px;overflow:hidden;background:var(--white)}
body{position:relative;font-family:"Raleway",sans-serif;color:var(--ink)}
.abs{position:absolute}

/* header */
.site-header{position:absolute;left:0;top:0;width:1200px;height:90px;background:var(--white)}
.brand{left:100px;top:28px;font-family:"Raleway",sans-serif;font-weight:800;font-size:27px;color:var(--navy);letter-spacing:-0.3px}
.nav-marker{left:540px;top:0;width:75px;height:6px;background:var(--green);border-radius:0 0 3px 3px}
.nav-link{top:39px;font-size:11.5px;font-weight:700;letter-spacing:1.6px;color:var(--ink);text-transform:uppercase}
.nav-link.active{color:var(--gold)}

/* hero */
.hero{left:0;top:90px;width:1200px;height:420px;background:linear-gradient(180deg,#8fb6d4 0%,#5f7e45 22%,#3f5a2c 45%,#7c6a52 62%,#8e7c66 80%,#6f5f4c 100%)}
.hero-title{left:250px;top:240px;font-family:"Open Sans Condensed","Open Sans",sans-serif;font-weight:700;font-size:48px;line-height:1;color:var(--white);letter-spacing:-1px}
.hero-sub{left:250px;top:290px;font-family:"Open Sans Condensed","Open Sans",sans-serif;font-weight:700;font-size:25px;line-height:1;color:var(--white);letter-spacing:-0.6px}

/* welcome */
.section-title{font-weight:800;font-size:39px;letter-spacing:2.2px;text-transform:uppercase;color:var(--ink);line-height:1}
.welcome-title{left:100px;top:567px}
.welcome-text{left:100px;top:646px;width:1000px;font-size:12px;line-height:21px;color:var(--muted)}

/* features */
.features{left:0;top:800px;width:1200px;height:295px;background:var(--soft)}
.feature{top:869px;width:322px}
.feature-kicker{font-family:"Lora",serif;font-style:italic;font-weight:600;font-size:12.5px;color:var(--gold)}
.feature-title{margin-top:10px;font-weight:700;font-size:16.5px;letter-spacing:1px;text-transform:uppercase;color:var(--ink)}
.feature-text{margin-top:17px;font-size:12px;line-height:21px;color:var(--muted)}

/* categories */
.categories{left:0;top:1095px;width:1200px;height:417px;background:var(--navy)}
.cat-kicker{left:102px;top:1135px;font-size:11px;font-weight:700;letter-spacing:1.5px;color:#a2a9bb;text-transform:uppercase}
.cat-title{left:101px;top:1174px;font-weight:800;font-size:36px;letter-spacing:1.8px;color:var(--white);text-transform:uppercase;line-height:1}
.cat-num{width:58px;height:58px;border-radius:50%;background:var(--gold);color:var(--white);font-family:"Open Sans",sans-serif;font-weight:600;font-size:34px;line-height:58px;text-align:center}
.cat-label{font-size:12px;font-weight:700;letter-spacing:1px;line-height:18px;color:var(--white);text-transform:uppercase}

/* products */
.products-title{left:98px;top:1584px;font-size:38px}
.product-photo{top:1681px;height:182px}
.product-name{top:1881px;font-size:12px;font-weight:700;letter-spacing:1.5px;color:var(--ink);text-transform:uppercase}
.product-btn{top:1917px;width:135px;height:38px;background:var(--gold);color:var(--white);font-size:10px;font-weight:700;letter-spacing:1.5px;text-align:center;line-height:38px;text-transform:uppercase}

/* footer */
.site-footer{left:0;top:2010px;width:1200px;height:222px;background:var(--navy)}
.footer-brand{left:501px;top:2048px;font-weight:800;font-size:27px;color:var(--gold);letter-spacing:-0.3px}
.footer-text{left:501px;top:2107px;width:230px;font-size:12px;line-height:20px;color:#c9cdd8}
.social{top:2181px;width:32px;height:32px;border-radius:50%;background:var(--white)}
</style>
</head>
<body>

<header class="site-header">
  <div class="abs brand">Halverton Blue Grid</div>
  <div class="abs nav-marker"></div>
  <nav>
    <span class="abs nav-link active" style="left:545px">Home</span>
    <span class="abs nav-link" style="left:630px">About</span>
    <span class="abs nav-link" style="left:720px">Product</span>
    <span class="abs nav-link" style="left:830px">Solutions</span>
    <span class="abs nav-link" style="left:951px">Contact</span>
    <svg class="abs" style="left:1041px;top:38px" width="14" height="13" viewBox="0 0 14 13" aria-label="Cart">
      <path d="M0 1h2.5l2 7h7l1.8-5H4" fill="none" stroke="#333" stroke-width="1.8"/>
      <circle cx="5.5" cy="11" r="1.3" fill="#333"/><circle cx="10.5" cy="11" r="1.3" fill="#333"/>
    </svg>
    <svg class="abs" style="left:1076px;top:38px" width="13" height="13" viewBox="0 0 13 13" aria-label="Search">
      <circle cx="5.2" cy="5.2" r="4" fill="none" stroke="#333" stroke-width="1.9"/>
      <path d="M8.2 8.2l3.8 3.8" stroke="#333" stroke-width="2"/>
    </svg>
  </nav>
</header>

<section>
  <div class="abs hero" role="img" aria-label="Photograph of a flooded road lined with trees, traffic cones and cars in the distance"></div>
  <h1 class="abs hero-title">DISTRIBUTOR</h1>
  <p class="abs hero-sub">OF DISASTER MANAGEMENT TECHNOLOGIES</p>
</section>

<section>
  <h2 class="abs section-title welcome-title">Welcome to Halverton Blue Grid</h2>
  <p class="abs welcome-text">Halverton Blue Grid provides safety related products, systems and services for the protection of people and property. Utilising world leading technologies for remote monitoring, collection of data and control of public warning infrastructure we are able to greatly improve situational awareness and help reduce the risk of injury and loss of life during emergency related events. Whether for general public warning or site specific applications we have the technology, expertise and experience to help you. The products available from Blue Grid come from highly regarded suppliers, are innovative in their designs and are suitable for a wide range of applications. They are designed for use in harsh environments and to function as intended in extreme events. From the acquisition of real time environmental data to the provision of equipment for mass notification to signage on mine sites, we can help you with your product needs.</p>
</section>

<section>
  <div class="abs features"></div>
  <div class="abs feature" style="left:100px">
    <p class="feature-kicker">We Are</p>
    <h3 class="feature-title">A Master Distribution House</h3>
    <p class="feature-text">Ut wisi enim ad minim veniam, quis nostrud exerci tation ullamcorper suscipit lobortis nisl ut aliquip ex ea commodo consequat. Duis autem vel eum iriure dolor in hendrerit in vulputate velit esse molestie consequat.</p>
  </div>
  <div class="abs feature" style="left:444px">
    <p class="feature-kicker">We Have</p>
    <h3 class="feature-title">Many Products</h3>
    <p class="feature-text">Ut wisi enim ad minim veniam, quis nostrud exerci tation ullamcorper suscipit lobortis nisl ut aliquip ex ea commodo consequat. Duis autem vel eum iriure dolor in hendrerit in vulputate velit esse molestie consequat.</p>
  </div>
  <div class="abs feature" style="left:786px">
    <p class="feature-kicker">We Offer</p>
    <h3 class="feature-title">Solutions and Services</h3>
    <p class="feature-text">Ut wisi enim ad minim veniam, quis nostrud exerci tation ullamcorper suscipit lobortis nisl ut aliquip ex ea commodo consequat. Duis autem vel eum iriure dolor in hendrerit in vulputate velit esse molestie consequat.</p>
  </div>
</section>

<section>
  <div class="abs categories"></div>
  <p class="abs cat-kicker">We have many products</p>
  <h2 class="abs cat-title">Product Categories</h2>

  <div class="abs cat-num" style="left:100px;top:1264px">1</div>
  <p class="abs cat-label" style="left:180px;top:1267px">Cloud based data<br>management</p>
  <div class="abs cat-num" style="left:358px;top:1264px">2</div>
  <p class="abs cat-label" style="left:437px;top:1267px">Remote camera's<br>and CCTV</p>
  <div class="abs cat-num" style="left:616px;top:1264px">3</div>
  <p class="abs cat-label" style="left:694px;top:1267px">Lighting and<br>beacons</p>
  <div class="abs cat-num" style="left:873px;top:1264px">4</div>
  <p class="abs cat-label" style="left:951px;top:1267px">Mass notification<br>and sirens</p>

  <div class="abs cat-num" style="left:100px;top:1373px">5</div>
  <p class="abs cat-label" style="left:180px;top:1376px">Cloud based data<br>management</p>
  <div class="abs cat-num" style="left:358px;top:1373px">6</div>
  <p class="abs cat-label" style="left:437px;top:1376px">Remote camera's<br>and CCTV</p>
  <div class="abs cat-num" style="left:616px;top:1373px">7</div>
  <p class="abs cat-label" style="left:694px;top:1376px">Lighting and<br>beacons</p>
  <div class="abs cat-num" style="left:873px;top:1373px">8</div>
  <p class="abs cat-label" style="left:951px;top:1376px">Mass notification<br>and sirens</p>
</section>

<section>
  <h2 class="abs section-title products-title">Disaster Management Products &amp; Solutions</h2>

  <div class="abs product-photo" style="left:97px;width:230px;background:linear-gradient(180deg,#5495c9,#4f8fc4)" role="img" aria-label="Photograph of a tall outdoor warning siren against a blue sky"></div>
  <div class="abs product-photo" style="left:352px;width:233px;background:linear-gradient(180deg,#d9d9d4 0%,#b8a25a 45%,#6d6a5e 100%)" role="img" aria-label="Photograph of a large yellow mining haul truck"></div>
  <div class="abs product-photo" style="left:612px;width:231px;background:linear-gradient(180deg,#8a8a72 0%,#6f7a4e 45%,#8b8378 100%)" role="img" aria-label="Photograph of a motorcyclist on a road washed out by flood water"></div>
  <div class="abs product-photo" style="left:870px;width:230px;background:linear-gradient(180deg,#f6f6f6 0%,#cfd7de 40%,#3a3a3a 100%)" role="img" aria-label="Photograph of tablets and a phone showing a monitoring map dashboard"></div>

  <p class="abs product-name" style="left:98px">Sirens</p>
  <p class="abs product-name" style="left:352px">Signage</p>
  <p class="abs product-name" style="left:612px">Camera</p>
  <p class="abs product-name" style="left:870px">Monitoring</p>

  <a class="abs product-btn" style="left:102px">Check it out</a>
  <a class="abs product-btn" style="left:358px">Check it out</a>
  <a class="abs product-btn" style="left:616px">Check it out</a>
  <a class="abs product-btn" style="left:873px">Check it out</a>
</section>

<footer>
  <div class="abs site-footer"></div>
  <div class="abs footer-brand">Halverton Blue Grid</div>
  <p class="abs footer-text">Lorem ipsum dolor sit amet, feugiat delicat liberavisse id cum no quo.</p>
  <span class="abs social" style="left:501px" aria-label="Social link"></span>
  <span class="abs social" style="left:546px" aria-label="Social link"></span>
  <span class="abs social" style="left:591px" aria-label="Social link"></span>
  <span class="abs social" style="left:635px" aria-label="Social link"></span>
</footer>

</body>
</html>
```